To design a look and feel for a website. The company offers technical services to governemtns and public bodies. It does NOT market to the public.

The core business is GIS (Geographic Information Systems)

The site needs to be clean and simple, The current version is available here: www.velda.ie

Target Market(s)

Goverment agencies and public bodies in the EU, buying through the public procurerment process

Requirements
Should not have
• corny graphics of hands holding globes or sateliites please.

```html
<!DOCTYPE html>
<html lang="en">
<head>
<meta charset="utf-8">
<title>The Velda Group – Information Expertise</title>
<link href="https://fonts.googleapis.com/css2?family=Ubuntu:wght@400;500;700&display=swap" rel="stylesheet">
<style>
:root{
  --navy:#1b2a4a;
  --navy-dark:#141f38;
  --navy-light:#3b4b6e;
  --gold:#c98d1a;
  --ink:#1e1e1e;
  --text:#2a2a2a;
  --muted:#8a8a8a;
  --soft:#a3a3a3;
  --rule:#dcdcdc;
  --band:#f6f6f6;
  --white:#ffffff;
}
*{margin:0;padding:0;box-sizing:border-box}
html,body{width:1185px;height:1200px;overflow:hidden;background:var(--white)}
body{position:relative;font-family:"Ubuntu",sans-serif;color:var(--text)}
.abs{position:absolute}

.utility-bar{left:0;top:0;width:1185px;height:28px;background:linear-gradient(#d4d4d4,#bdbdbd)}
.utility-bar a{position:absolute;top:6px;font-size:13px;color:var(--white);text-decoration:none}
.brand-stripe{top:28px;left:16px;width:1149px;height:5px;background:linear-gradient(90deg,var(--navy) 0 67.3%,var(--gold) 67.3% 100%)}

.main-nav{left:16px;top:58px;height:74px;display:flex}
.main-nav a{display:block;height:74px;padding:18px 16px 0;font-size:16px;color:var(--ink);text-decoration:none;border-right:1px dotted #cfcfcf}
.main-nav a:last-child{border-right:none}

.brand{left:905px;top:54px;width:190px;text-align:center;color:var(--navy);line-height:1}
.brand-name{font-size:28px;font-weight:700;letter-spacing:1px;white-space:nowrap}
.brand-group{font-size:17px;font-weight:700;letter-spacing:2px;margin-top:2px}
.brand-sub{font-size:13px;font-weight:500;margin-top:5px;white-space:nowrap}

.header-rule{left:16px;top:155px;width:1149px;height:1px;background:var(--rule)}

.hero-visual{left:16px;top:193px;width:406px;height:304px;background:linear-gradient(135deg,#ffffff,#e7e7e7 60%,#cfcfcf)}
.hero-title{left:446px;top:205px;font-size:31px;font-weight:400;color:var(--ink)}
.hero-copy{left:446px;top:259px;width:272px;font-size:20.5px;line-height:27px;color:var(--soft)}
.hero-copy p+p{margin-top:15px}
.more-link{display:inline-flex;align-items:center;font-size:12.5px;font-weight:700;color:var(--gold);text-transform:uppercase;letter-spacing:.2px}
.more-link::before{content:"";width:3px;height:12px;background:var(--gold);margin-right:14px}
.hero-more{left:446px;top:452px}

.slide-tabs{left:16px;top:512px;width:534px;height:60px;border-top:1px solid #e6e6e6;display:flex}
.slide-tab{width:131px;text-align:center;font-size:15px;line-height:23px;padding-top:12px;color:var(--muted)}
.slide-tab.is-active{background:linear-gradient(#ffffff,#ececec);color:var(--ink)}
.slide-rule{left:16px;top:571px;width:708px;height:1px;background:#e6e6e6}
.slide-controls{left:580px;top:524px}

.column-divider{left:775px;top:181px;width:1px;height:416px;background:#e4e4e4}

.clients-head{left:798px;top:181px;width:349px;height:49px;border-top:1px solid #e4e4e4;background:linear-gradient(#ffffff,#f1f1f1);padding:13px 12px;font-size:21px;font-weight:500;color:var(--gold)}
.clients-board{left:799px;top:241px;width:348px;height:195px;border:5px solid var(--navy);background:var(--white);display:grid;grid-template-columns:repeat(4,1fr);grid-template-rows:repeat(3,1fr);align-items:center;justify-items:center;padding:6px}
.client-name{font-size:11px;font-weight:500;color:var(--navy);text-align:center;line-height:13px}
.clients-list{left:808px;top:455px;list-style:none;font-size:15px;line-height:23.2px;color:var(--ink)}
.see-more{left:800px;top:585px;color:var(--ink)}
.see-more::before{background:var(--ink)}

.services-band{left:16px;top:611px;width:1149px;height:378px;background:var(--band);border-bottom:1px solid #e0e0e0}
.service-card{top:622px;width:252px}
.service-head{height:48px;background:linear-gradient(var(--navy-light),var(--navy-dark));color:var(--white);font-size:17px;font-weight:700;text-align:center;line-height:48px}
.service-visual{height:139px;background:linear-gradient(160deg,#e9e7e2,#b9b3a8 70%,#8a8379)}
.service-text{margin-top:8px;font-size:15.4px;line-height:23.2px;color:var(--ink)}
.service-card .more-link{position:absolute;top:331px;left:0}

.site-footer{left:16px;top:1015px;width:1149px;height:185px;background:linear-gradient(#eeeeee,#f9f9f9 30%,#fafafa)}
.footer-heading{font-size:18px;font-weight:700;color:#8e8e8e;top:1029px}
.footer-info{left:34px;top:1075px;font-size:14px;line-height:23.2px;color:var(--muted)}
.footer-links{left:616px;top:1081px;list-style:none;font-size:14px;line-height:23.2px;color:var(--muted)}
.footer-links li::before{content:"";display:inline-block;width:4px;height:4px;background:#9a9a9a;margin-right:8px;vertical-align:middle}
.social{left:900px;top:1075px;display:grid;grid-template-columns:repeat(5,36px);gap:11px 10px}
.social span{width:36px;height:36px;border-radius:50%;background:linear-gradient(#ffffff,#dcdcdc);box-shadow:0 3px 4px rgba(0,0,0,.25);font-size:8.5px;font-weight:700;color:#333;display:flex;align-items:center;justify-content:center}
</style>
</head>
<body>

<header>
  <div class="abs utility-bar"><a href="#" style="left:21px">Home</a><a href="#" style="left:74px">Sitemap</a></div>
  <div class="abs brand-stripe"></div>
  <nav class="abs main-nav">
    <a href="#">HOME</a><a href="#">SERVICES</a><a href="#">CLIENTS</a><a href="#">CONTACT</a><a href="#">INSPIRE</a>
  </nav>
  <div class="abs brand">
    <div class="brand-name">THE VELDA</div>
    <div class="brand-group">GROUP</div>
    <div class="brand-sub">Information Expertise</div>
  </div>
  <div class="abs header-rule"></div>
</header>

<main>
  <section class="hero">
    <div class="abs hero-visual" role="img" aria-label="Silver bar chart with a declining arrow"></div>
    <h1 class="abs hero-title">Lorem Ipsum dolor</h1>
    <div class="abs hero-copy">
      <p>Lorem Ipsum dolor Lorem Ipsum dolor Lorem Ipsum dolor Lorem Ipsum dolor.</p>
      <p>Lorem Ipsum dolor Lorem Ipsum dolor Lorem Ipsum dolor Lorem Ipsum dolor.</p>
    </div>
    <a class="abs more-link hero-more">Lorem Ipsum dolor</a>
    <div class="abs slide-tabs">
      <div class="slide-tab is-active">Lorem Ipsum<br>dolor</div>
      <div class="slide-tab">Lorem Ipsum<br>dolor</div>
    </div>
    <div class="abs slide-rule"></div>
    <svg class="abs slide-controls" width="120" height="34" viewBox="0 0 120 34">
      <defs><linearGradient id="btn" x1="0" y1="0" x2="0" y2="1"><stop offset="0" stop-color="#f4f4f4"/><stop offset="1" stop-color="#b9b9b9"/></linearGradient></defs>
      <rect x="2" y="3" width="28" height="28" rx="8" fill="url(#btn)" stroke="#8a8a8a"/>
      <circle cx="16" cy="17" r="10" fill="none" stroke="#222" stroke-width="1.6"/>
      <path d="M19 12l-6 5 6 5z" fill="#222"/>
      <rect x="38" y="3" width="28" height="28" rx="8" fill="url(#btn)" stroke="#8a8a8a"/>
      <circle cx="52" cy="17" r="10" fill="none" stroke="#222" stroke-width="1.6"/>
      <path d="M49 12l6 5-6 5z" fill="#222"/>
      <rect x="84" y="1" width="30" height="32" rx="6" fill="url(#btn)" stroke="#8a8a8a"/>
      <rect x="93" y="9" width="4" height="16" fill="#222"/><rect x="101" y="9" width="4" height="16" fill="#222"/>
    </svg>
  </section>

  <div class="abs column-divider"></div>

  <aside>
    <h2 class="abs clients-head">Our Clients</h2>
    <div class="abs clients-board">
      <span class="client-name">Coach Linea</span>
      <span class="client-name">Agri Council</span>
      <span class="client-name">Harbour Bus</span>
      <span class="client-name">State Office</span>
      <span class="client-name">Orbis Data</span>
      <span class="client-name">Enviro Dept</span>
      <span class="client-name">Global Assembly</span>
      <span class="client-name">Forest Board</span>
      <span class="client-name">Research Hub</span>
      <span class="client-name">Statis EU</span>
      <span class="client-name">Transit Forum</span>
      <span class="client-name">Health Board</span>
    </div>
    <ol class="abs clients-list">
      <li>1.Bureau of Statistics (Valdoria),</li>
      <li>2.Coach Linea,Dept of Farming (Area Aid),</li>
      <li>3.Dept. of Learning,</li>
      <li>4.Dept of Estates (Property Branch).</li>
      <li>5.Harbour Bus</li>
    </ol>
    <a class="abs more-link see-more">See More</a>
  </aside>

  <section>
    <div class="abs services-band"></div>
    <article class="abs service-card" style="left:34px">
      <h3 class="service-head">Data Management</h3>
      <div class="service-visual" role="img" aria-label="Modern interior with staircase and yellow chairs"></div>
      <p class="service-text">Lorem Ipsum dolor Lorem Ipsum dolor Lorem Ipsum dolor Lorem Ipsum dolor Lorem Ipsum dolor Lorem Ipsum dolor Lorem Ipsum dolor</p>
      <a class="more-link">Read More</a>
    </article>
    <article class="abs service-card" style="left:320px">
      <h3 class="service-head">Spatial Data</h3>
      <div class="service-visual" role="img" aria-label="Dining room with dark table and white cabinets"></div>
      <p class="service-text">Lorem Ipsum dolor Lorem Ipsum dolor Lorem Ipsum dolor Lorem Ipsum dolor Lorem Ipsum dolor Lorem Ipsum dolor Lorem Ipsum dolor.</p>
      <a class="more-link">Read More</a>
    </article>
    <article class="abs service-card" style="left:607px">
      <h3 class="service-head">Land Use</h3>
      <div class="service-visual" role="img" aria-label="Bright living room with white sofas and tall windows"></div>
      <p class="service-text">Lorem Ipsum dolor Lorem Ipsum dolor Lorem Ipsum dolor Lorem Ipsum dolor Lorem Ipsum dolor Lorem Ipsum dolor Lorem Ipsum dolor</p>
      <a class="more-link">Read More</a>
    </article>
    <article class="abs service-card" style="left:893px">
      <h3 class="service-head">Transport</h3>
      <div class="service-visual" role="img" aria-label="Lounge with grey sofas and stone wall"></div>
      <p class="service-text">Lorem Ipsum dolor Lorem Ipsum dolor Lorem Ipsum dolor Lorem Ipsum dolor Lorem Ipsum dolor Lorem Ipsum dolor Lorem Ipsum dolor</p>
      <a class="more-link">Read More</a>
    </article>
  </section>
</main>

<footer>
  <div class="abs site-footer"></div>
  <h4 class="abs footer-heading" style="left:34px">Company Info</h4>
  <div class="abs footer-info">
    Copyright © VELDA GROUP 2013-14. All rights reserved.<br>
    Corporate: 00 (000) 000-0000<br>
    Toll Free: 0000 000 000 0000<br>
    Lane<br>
    city, Country
  </div>
  <h4 class="abs footer-heading" style="left:608px">Important Links</h4>
  <ul class="abs footer-links">
    <li>Important Link 1</li><li>Important Link 2</li><li>Important Link 3</li><li>Important Link 4</li>
  </ul>
  <h4 class="abs footer-heading" style="left:894px">Contact &amp; Follow Us</h4>
  <div class="abs social">
    <span>Post</span><span>Feed</span><span>Chirpo</span><span>Page</span><span>Linkro</span>
    <span>Pixo</span><span>Gridly</span><span>Diggo</span><span>Stumbo</span><span>Add</span>
  </div>
</footer>

</body>
</html>
```